Business card design for an Art Director working for museums

The business card design we're looking for is for an Art Director in a private museum called "OLV Gallery". The museum showcases artworks made by the country's national artists. Designs should use the CMYK "0 40 100 20". You have the liberty to use any type you want except for overly decorative ones.

Target Market(s)

Professional and creative individuals. Interior designers, museum curators, museum coordinators etc

Industry/Entity Type

Museum

Contact Information for Business Card

Rel T
Art Director
+1 555 374 9281

Font styles to use
Serif
Sans Serif
Script

Requirements
Must have
• My project must have the CMYK 0 40 100 20. You can play with the Key.
• We're keen on clean, minimal, and architectural-type design.
Nice to have
• Geometric gradients that nicely complement the main CMYK that we've posted.
Should not have
• Off-putting colour palettes

```html
<!DOCTYPE html>
<html lang="en">
<head>
<meta charset="utf-8">
<title>OLV Gallery – Business Card</title>
<link rel="stylesheet" href="https://fonts.googleapis.com/css2?family=Poppins:wght@600&family=Courier+Prime&display=swap">
<style>
  :root {
    --page-bg: #ffffff;
    --card-bg: #3e3425;
    --card-bg-deep: #352c1f;
    --card-bg-light: #463b2b;
    --brand-amber: #cf8818;
    --divider-gold: #e2b45c;
    --ink-light: #ffffff;
  }
  html, body {
    margin: 0;
    padding: 0;
    width: 1200px;
    height: 960px;
    overflow: hidden;
    background: var(--page-bg);
  }
  .canvas {
    position: relative;
    width: 1200px;
    height: 960px;
  }
  .card {
    position: absolute;
    left: 329px;
    width: 543px;
    height: 311px;
    background: var(--card-bg);
    overflow: hidden;
  }
  .card--front { top: 133px; }
  .card--back  { top: 523px; box-shadow: -3px 0 3px rgba(0,0,0,0.12); }

  .brand-name {
    position: absolute;
    left: 12px;
    right: 0;
    margin: 0;
    text-align: center;
    font-family: "Poppins", sans-serif;
    font-weight: 600;
    font-size: 30px;
    line-height: 1;
    letter-spacing: 0.5px;
    color: var(--brand-amber);
  }
  .card--front .brand-name { top: 141px; }
  .card--back .brand-name  { top: 147px; }

  .person-name {
    position: absolute;
    right: 288px;
    top: 229px;
    margin: 0;
    font-family: "Courier Prime", monospace;
    font-size: 29px;
    line-height: 1;
    letter-spacing: 5px;
    color: var(--ink-light);
    white-space: nowrap;
  }
  .divider {
    position: absolute;
    left: 271px;
    top: 219px;
    width: 2px;
    height: 55px;
    background: var(--divider-gold);
  }
  .contact {
    position: absolute;
    left: 290px;
    top: 226px;
    margin: 0;
    font-family: "Courier Prime", monospace;
    font-size: 14px;
    line-height: 22px;
    letter-spacing: 1.6px;
    color: var(--ink-light);
    white-space: nowrap;
  }
  .contact span { display: block; }

  .back-texture {
    position: absolute;
    inset: 0;
    background: linear-gradient(135deg, var(--card-bg-deep) 0%, var(--card-bg) 45%, var(--card-bg-light) 60%, var(--card-bg-deep) 100%);
  }
</style>
</head>
<body>
<main class="canvas">
  <section class="card card--front">
    <h1 class="brand-name">OLV GALLERY</h1>
    <p class="person-name">REL T.</p>
    <div class="divider"></div>
    <p class="contact">
      <span class="contact-role">ART DIRECTOR</span>
      <span class="contact-phone">+1 555 374 9281</span>
    </p>
  </section>

  <section class="card card--back">
    <div class="back-texture" role="img" aria-label="Faint geometric faceted pattern in dark brown tones"></div>
    <p class="brand-name">OLV GALLERY</p>
  </section>
</main>
</body>
</html>
```